Varnelux7 website

Need to create a website for my business

Target Market(s)

Food ingredient companies, B2B

Industry/Entity Type

Food technology, food ingredients

Coding

Number of Pages Required

2 page

Requirements
Nice to have
• Case studies, links to articles,

```html
<!DOCTYPE html>
<html lang="en">
<head>
<meta charset="utf-8">
<title>Varnelux7 — Results Matter. Work Hard.</title>
<link href="https://fonts.googleapis.com/css2?family=Montserrat:wght@500;600;700;800&family=Poppins:wght@400;500;600&display=swap" rel="stylesheet">
<style>
:root{
  --green:#0b7a10;
  --green-dark:#06660b;
  --green-deep:#045208;
  --text:#333333;
  --muted:#7a7a7a;
  --white:#ffffff;
  --light:#f4f7f2;
}
*{box-sizing:border-box;margin:0;padding:0}
html,body{width:1200px;height:4396px;overflow:hidden;background:var(--white)}
body{font-family:"Poppins",sans-serif;color:var(--text)}
.page{position:relative;width:1200px;height:4396px;overflow:hidden}
.abs{position:absolute}
a{color:inherit;text-decoration:none}

/* header */
.brand{position:absolute;display:flex;align-items:center;gap:14px}
.brand-dot{width:30px;height:30px;border-radius:50%;background:var(--green)}
.brand-name{font-family:"Montserrat",sans-serif;font-weight:600;color:#333;letter-spacing:2px}
.brand-tag{font-size:15px;color:#333;font-family:"Montserrat",sans-serif;font-weight:500}
.site-brand{left:128px;top:40px}
.site-brand .brand-name{font-size:26px;line-height:30px}
.nav{position:absolute;top:82px;left:456px;display:flex;gap:0;font-family:"Montserrat",sans-serif;font-size:13px;font-weight:500;color:#555}
.nav a{position:absolute;white-space:nowrap}
.call{position:absolute;right:137px;top:26px;display:flex;align-items:center;gap:8px;font-family:"Montserrat",sans-serif;font-weight:700;font-size:20px;color:var(--green)}

/* hero */
.hero-photo{left:0;top:0;width:1200px;height:760px;background:linear-gradient(100deg,#ffffff 0%,#fbfcf8 30%,#e4eed6 50%,#a9c98c 72%,#5f9a46 100%)}
.hero-title{left:133px;top:266px;font-family:"Montserrat",sans-serif;font-weight:800;font-size:60px;color:var(--green);letter-spacing:.5px}
.hero-sub{left:140px;top:340px;width:440px;font-family:"Montserrat",sans-serif;font-weight:700;font-size:26px;line-height:36px;color:#222}
.tech-title{left:669px;top:770px;font-family:"Montserrat",sans-serif;font-weight:800;font-size:48px;color:var(--white)}
.tech-text{left:669px;top:852px;width:440px;font-size:16.5px;line-height:21.5px;color:var(--white)}
.btn{position:absolute;display:flex;align-items:center;justify-content:center;font-family:"Montserrat",sans-serif;font-weight:600;font-size:15px;letter-spacing:.5px;border-radius:0 18px 0 18px}
.btn-outline{border:2px solid var(--white);color:var(--white)}
.btn-solid{background:var(--green);color:var(--white)}

/* about */
.section-title{position:absolute;font-family:"Montserrat",sans-serif;font-weight:800;color:var(--green)}
.about-title{left:150px;top:1426px;font-size:48px}
.about-text{left:151px;top:1511px;width:540px;font-size:17px;line-height:21.5px;color:#444}
.about-text p+p{margin-top:22px}
.about-mark{left:780px;top:1420px;width:300px;height:380px;display:flex;flex-direction:column;align-items:center;justify-content:center;gap:20px}
.about-mark .circle{width:120px;height:120px;border-radius:50%;background:var(--green)}
.about-mark span{font-family:"Montserrat",sans-serif;font-weight:700;font-size:44px;color:var(--green)}

/* what we do */
.wwd-title{left:0;width:1200px;top:2022px;text-align:center;font-size:46px;color:var(--white)}
.service{position:absolute;width:300px;text-align:center;color:var(--white)}
.service-icon{width:146px;height:146px;margin:0 auto;border:2px solid var(--white);border-radius:50%;display:flex;align-items:center;justify-content:center}
.service h3{margin-top:32px;font-family:"Montserrat",sans-serif;font-weight:700;font-size:19px;line-height:22px}
.service p{margin-top:20px;font-size:14.5px;line-height:21.5px}

/* case studies */
.cs-title{left:0;width:1200px;top:2758px;text-align:center;font-size:48px}
.cs-sub{left:0;width:1200px;top:2843px;text-align:center;font-size:17px;line-height:22px;color:#444}
.card{position:absolute;top:2919px;width:321px}
.card-img{width:321px;height:248px}
.card h3{margin-top:28px;font-family:"Montserrat",sans-serif;font-weight:700;font-size:19.5px;line-height:22px;color:#333}
.card .date{margin-top:20px;font-size:14px;color:var(--muted)}
.card p{margin-top:14px;font-size:14.5px;line-height:21px;color:#555}
.card .more{display:block;margin-top:22px;font-family:"Montserrat",sans-serif;font-weight:700;font-size:14px;color:var(--green)}

/* cta */
.cta-photo{left:0;top:3585px;width:1200px;height:582px;background:linear-gradient(180deg,#ffffff 0%,#eef2f2 25%,#d9e3e4 50%,#c7d2b4 68%,#6f8d3a 80%,#3f6a1c 100%)}
.cta-title{left:0;width:1200px;top:3740px;text-align:center;font-size:50px;line-height:56px}

/* footer */
.foot-brand{left:145px;top:4228px}
.foot-brand .brand-name{font-size:22px;line-height:26px}
.foot-brand .brand-tag{font-size:12px}
.foot-link{position:absolute;font-size:13.5px;color:#333}
.social{position:absolute;top:4213px;width:18px;height:18px;border-radius:50%;background:#b5b5b5}
.copyright{left:0;width:1200px;top:4362px;text-align:center;font-size:13px;color:#444}
</style>
</head>
<body>
<div class="page">

  <!-- hero background -->
  <div class="abs hero-photo" role="img" aria-label="Hand holding a smartphone above a field of young green crops"></div>

  <header>
    <div class="brand site-brand">
      <div class="brand-dot"></div>
      <div>
        <div class="brand-name">VARNELUX7</div>
        <div class="brand-tag">Results Matter. Work Hard.</div>
      </div>
    </div>
    <div class="call">
      <svg width="26" height="24" viewBox="0 0 26 24"><path d="M3 22 C1 10 10 2 24 2 C24 14 16 22 3 22Z" fill="var(--green)"/></svg>
      CALL US: 555 0142 310
    </div>
    <nav class="nav">
      <a style="left:0;color:var(--green)">HOME</a>
      <a style="left:85px">ABOUT US</a>
      <a style="left:199px">WHY US</a>
      <a style="left:296px">SERVICES</a>
      <a style="left:406px">CASE STUDIES</a>
      <a style="left:544px">CONTACT</a>
    </nav>
  </header>

  <h1 class="abs hero-title">VARNELUX7</h1>
  <p class="abs hero-sub">Lorem ipsum dolor sit amet, consectetur adipiscing elitdo eiusmod tempor</p>

  <!-- technology wave -->
  <svg class="abs" style="left:0;top:560px" width="1200" height="690" viewBox="0 560 1200 690">
    <path d="M0 750 C200 700 350 690 500 680 C700 665 850 560 1000 570 C1100 575 1160 588 1200 600 L1200 1220 C1000 1225 700 1210 560 1235 C400 1230 150 1080 0 1005 Z" fill="var(--green)"/>
    <path d="M120 760 C260 640 470 660 540 740 C600 820 560 950 580 1060 C600 1170 520 1235 420 1235 Z" fill="var(--green-dark)" opacity=".6"/>
  </svg>
  <svg class="abs" style="left:70px;top:650px" width="500" height="600" viewBox="70 650 500 600" role="img" aria-label="Robotic camera inspecting ripe tomatoes on the vine while a farmer holds a tablet">
    <defs>
      <linearGradient id="blobFill" x1="0" y1="0" x2="1" y2="1">
        <stop offset="0" stop-color="#dfe6dc"/>
        <stop offset=".45" stop-color="#6f9a4a"/>
        <stop offset=".75" stop-color="#c8442c"/>
        <stop offset="1" stop-color="#3e6a2a"/>
      </linearGradient>
    </defs>
    <path d="M130 800 C200 690 380 640 470 700 C560 760 520 880 530 980 C545 1120 470 1235 330 1232 C180 1228 80 1120 77 990 C75 900 95 850 130 800 Z" fill="url(#blobFill)"/>
  </svg>

  <h2 class="abs tech-title">TECHNOLOGY</h2>
  <p class="abs tech-text">Lorem ipsum dolor sit amet, consecteturadipiscing elit, sed do eiusmod tempor incididunt ut labore et dolore magnaua. Quis ipsum suspendisse ultrices gravida. Risus commodo viverra maecenas acc umsan lacus vel facilisivel facilisis. Lorem ipsum dolor sit amet, consecteturadipiscing elit, sed do eiusmod tempor incididunt ut labore et dolore magnaua. Quis ipsum suspendisse ultrices grav ida. Risus commodo viverra</p>
  <a class="btn btn-outline" style="left:669px;top:1079px;width:164px;height:48px">READ MORE</a>

  <!-- about -->
  <h2 class="section-title about-title">ABOUT US</h2>
  <div class="abs about-text">
    <p>Lorem ipsum dolor sit amet, consectetur adipiscing elit, sed do eiusmod tempor incididunt ut labore et dolore magna aliqua. Quis ipsum suspendisse ultrices gravida. Risus commodo viverra maecenas accumsan lacus vel facilisis.</p>
    <p>Lorem ipsum dolor sit amet, consectetur adipiscing elit, sed do eiusmod tempor incididunt ut labore et dolore magna aliqua. Quis ipsum suspendisse ultrices gravida. Risus commodo viverra maecenas accumsan lacus vel facilisis.</p>
  </div>
  <a class="btn btn-solid" style="left:151px;top:1738px;width:163px;height:46px">READ MORE</a>
  <div class="abs about-mark">
    <div class="circle"></div>
    <span>Varnelux7</span>
  </div>

  <!-- what we do -->
  <svg class="abs" style="left:0;top:1915px" width="1200" height="755" viewBox="0 1915 1200 755" role="img" aria-label="Rows of green crops in a field behind a green overlay">
    <defs>
      <linearGradient id="wwdFill" x1="0" y1="0" x2="0" y2="1">
        <stop offset="0" stop-color="#0b7a10"/>
        <stop offset=".55" stop-color="#0a7510"/>
        <stop offset=".8" stop-color="#2a8a1e"/>
        <stop offset="1" stop-color="#0a6a0e"/>
      </linearGradient>
    </defs>
    <path d="M0 1990 C400 1900 800 1900 1200 1990 L1200 2552 C800 2700 400 2690 0 2578 Z" fill="url(#wwdFill)"/>
  </svg>
  <h2 class="section-title wwd-title">WHAT WE DO</h2>

  <div class="service" style="left:135px;top:2158px">
    <div class="service-icon">
      <svg width="74" height="74" viewBox="0 0 74 74" fill="none" stroke="#fff" stroke-width="2.5" stroke-linecap="round" stroke-linejoin="round">
        <path d="M37 40 V20"/><path d="M37 26 C30 14 20 18 22 26 C26 30 33 30 37 26Z"/><path d="M37 22 C44 10 54 14 52 22 C48 26 41 26 37 22Z"/>
        <path d="M10 42 C16 52 26 62 37 62 C48 62 58 52 64 42"/><path d="M20 44 L28 52"/><path d="M54 44 L46 52"/>
      </svg>
    </div>
    <h3>LOREM IPSM DO<br>LOR LORIT AMECONSE</h3>
    <p>Lorem ipsum dolor sit amet, conse ctetur adipiscing elit, sed d eiusm od tempor incididunt ut labore et dolore magna aliquuis ipsum</p>
  </div>
  <div class="service" style="left:451px;top:2158px">
    <div class="service-icon">
      <svg width="74" height="74" viewBox="0 0 74 74" fill="none" stroke="#fff" stroke-width="2.5" stroke-linecap="round" stroke-linejoin="round">
        <rect x="20" y="24" width="34" height="30" rx="8"/><rect x="30" y="32" width="14" height="14"/>
        <path d="M37 24 V12"/><path d="M37 14 C42 8 48 10 48 12 C44 16 40 16 37 14Z"/>
        <path d="M12 34 H20 M12 44 H20 M54 34 H62 M54 44 H62 M30 54 V62 M44 54 V62"/>
      </svg>
    </div>
    <h3>LOREM IPSM DO<br>LOR LORIT AMECONSE</h3>
    <p>Lorem ipsum dolor sit amet, conse ctetur adipiscing elit, sed d eiusm od tempor incididunt ut labore et dolore magna aliquuis ipsum</p>
  </div>
  <div class="service" style="left:768px;top:2158px">
    <div class="service-icon">
      <svg width="74" height="74" viewBox="0 0 74 74" fill="none" stroke="#fff" stroke-width="2.5" stroke-linecap="round" stroke-linejoin="round">
        <path d="M22 10 H52 M30 10 V16 H44 V10"/><path d="M37 16 V26"/><path d="M31 26 H43 L40 34 H34 Z"/>
        <circle cx="37" cy="42" r="5"/>
        <rect x="12" y="52" width="50" height="12" rx="6"/><circle cx="22" cy="58" r="2.5"/><circle cx="37" cy="58" r="2.5"/><circle cx="52" cy="58" r="2.5"/>
      </svg>
    </div>
    <h3>LOREM IPSM DO<br>LOR LORIT AMECONSE</h3>
    <p>Lorem ipsum dolor sit amet, conse ctetur adipiscing elit, sed d eiusm od tempor incididunt ut labore et dolore magna aliquuis ipsum</p>
  </div>

  <!-- case studies -->
  <h2 class="section-title cs-title">CASE STUDIES</h2>
  <p class="abs cs-sub">Lorem ipsum dolor sit amet, consectetur adipiscing elit, sed do eiusmod<br>tempor incididunt ut labore et dolore magna aliqua. Quis ipsum</p>

  <article class="card" style="left:73px">
    <div class="card-img" role="img" aria-label="Farmer using a tablet beside a tomato-picking robot in a greenhouse" style="background:linear-gradient(135deg,#5d8a3c,#b8c4b0 45%,#c0473a 70%,#7a4a3e)"></div>
    <h3>Lorem ipsum dolor sit ame consectetur adipiscg</h3>
    <div class="date">Case studies: Apr 1 2022</div>
    <p>Lorem ipsum dolor sit amet, conse ctetur adipiscing elit, sed d eiusm od tempor incididunt ut labore et dolore magna aliquuis ipsum</p>
    <a class="more">Read More &rsaquo;</a>
  </article>
  <article class="card" style="left:440px">
    <div class="card-img" role="img" aria-label="Young corn plants in a field under a blue sky with digital overlay circles" style="background:linear-gradient(180deg,#3d84d0,#9cc5ea 40%,#6e9b3f 65%,#4e3b28)"></div>
    <h3>Lorem ipsum dolor sit ame consectetur adipiscg</h3>
    <div class="date">Case studies: Apr 1 2022</div>
    <p>Lorem ipsum dolor sit amet, conse ctetur adipiscing elit, sed d eiusm od tempor incididunt ut labore et dolore magna aliquuis ipsum</p>
    <a class="more">Read More &rsaquo;</a>
  </article>
  <article class="card" style="left:806px">
    <div class="card-img" role="img" aria-label="Workers in white coats checking products in a food processing plant" style="background:linear-gradient(135deg,#e6e4df,#bdb8b0 50%,#7f7a72)"></div>
    <h3>Lorem ipsum dolor sit ame consectetur adipiscg</h3>
    <div class="date">Case studies: Apr 1 2022</div>
    <p>Lorem ipsum dolor sit amet, conse ctetur adipiscing elit, sed d eiusm od tempor incididunt ut labore et dolore magna aliquuis ipsum</p>
    <a class="more">Read More &rsaquo;</a>
  </article>

  <a class="btn btn-solid" style="left:507px;top:3472px;width:186px;height:46px">VIEW ARTICLES</a>

  <!-- call to action -->
  <div class="abs cta-photo" role="img" aria-label="Rows of crops in a wide field under a bright hazy sky"></div>
  <h2 class="section-title cta-title">LOREM IPSUM DOLOR SIT<br>AMET, CONSECTETUR</h2>
  <a class="btn btn-solid" style="left:519px;top:3853px;width:160px;height:46px">GET STARTED</a>

  <!-- footer -->
  <footer>
    <div class="brand foot-brand">
      <div class="brand-dot" style="width:24px;height:24px"></div>
      <div>
        <div class="brand-name">VARNELUX7</div>
        <div class="brand-tag">Results Matter. Work Hard.</div>
      </div>
    </div>
    <a class="foot-link" style="left:423px;top:4228px">Latest News</a>
    <a class="foot-link" style="left:423px;top:4254px">Why Us?</a>
    <a class="foot-link" style="left:423px;top:4280px">About Us</a>
    <a class="foot-link" style="left:561px;top:4228px">Resources</a>
    <a class="foot-link" style="left:561px;top:4254px">Contact Us</a>
    <a class="foot-link" style="left:561px;top:4280px">Latest News</a>
    <a class="foot-link" style="left:703px;top:4228px">What we do</a>
    <a class="foot-link" style="left:703px;top:4254px">Technology</a>
    <a class="foot-link" style="left:703px;top:4280px">Articles</a>
    <span class="social" style="left:881px"></span>
    <span class="social" style="left:930px"></span>
    <span class="social" style="left:979px"></span>
    <span class="social" style="left:1028px"></span>
    <a class="btn btn-solid" style="left:881px;top:4259px;width:162px;height:44px">CONTACT NOW</a>
    <p class="abs copyright">© 2022 Varnelux7 . All Rights Reserved</p>
  </footer>

</div>
</body>
</html>
```